CaptainKettle needs a new packaging

We are Coffee Roasters based in Versailles France.

We want a new design for our coffee packaging. The packaging is a basic brown paper bag. We are sticking on it a 99.1mm x 67.7mm Label.

We want a new design for the label. The label should have the following info : Name of the coffee, origin, one line of description, our website www.captainkettle.fr.

Enclosed you will find our logo, as well as a picture of our current packaging

The Design should be "simple yet sophisticate".

```html
<!DOCTYPE html>
<html lang="fr">
<head>
<meta charset="utf-8">
<title>CaptainKettle – Étiquette N°5</title>
<link href="https://fonts.googleapis.com/css2?family=Old+Standard+TT:ital,wght@0,400;0,700;1,400&family=Josefin+Sans:wght@400&display=swap" rel="stylesheet">
<style>
  :root {
    --ink: #2b2628;
    --kraft: #cfc19a;
    --kraft-deep: #c6b78f;
  }
  * { margin: 0; padding: 0; box-sizing: border-box; }
  html, body { width: 1200px; height: 820px; overflow: hidden; background: var(--ink); }
  .label {
    position: relative;
    width: 1200px; height: 820px;
    background: var(--ink);
    font-family: "Old Standard TT", "Century Schoolbook", serif;
    color: var(--ink);
  }
  .label__paper {
    position: absolute; left: 20px; top: 20px; right: 20px; bottom: 20px;
    background: radial-gradient(ellipse at center, var(--kraft) 0%, var(--kraft-deep) 100%);
  }
  .label__frame {
    position: absolute; left: 40px; top: 36px; right: 40px; bottom: 36px;
    border: 5px solid var(--ink);
  }
  .brand {
    position: absolute; top: 98px; left: 0; right: 0;
    display: flex; justify-content: center; align-items: center; gap: 18px;
  }
  .brand__dot {
    width: 86px; height: 86px; border-radius: 50%; background: var(--ink);
  }
  .brand__text { display: flex; flex-direction: column; }
  .brand__name {
    font-weight: 700; font-size: 58px; line-height: 1;
    padding-bottom: 6px; border-bottom: 3px solid var(--ink);
  }
  .brand__tagline {
    font-family: "Josefin Sans", Arial, sans-serif;
    font-size: 24px; margin-top: 8px; padding-left: 2px;
  }
  .line { position: absolute; left: 0; right: 0; text-align: center; white-space: nowrap; }
  .coffee-name { top: 266px; font-size: 80px; font-weight: 700; line-height: 1; }
  .coffee-name sup { font-size: 0.5em; vertical-align: 0.8em; }
  .coffee-type { top: 368px; font-size: 38px; font-weight: 700; }
  .coffee-origin { top: 414px; font-size: 38px; font-weight: 700; }
  .coffee-desc { top: 503px; font-size: 29px; font-style: italic; }
  .address { top: 584px; font-size: 27px; font-weight: 700; }
  .phone { top: 625px; font-size: 27px; font-weight: 700; }
  .website { top: 660px; font-size: 66px; font-weight: 700; }
</style>
</head>
<body>
<main class="label">
  <div class="label__paper" role="img" aria-label="Kraft background with a faint repeating coffee bean pattern"></div>
  <div class="label__frame"></div>

  <header class="brand">
    <span class="brand__dot"></span>
    <div class="brand__text">
      <span class="brand__name">CaptainKettle</span>
      <span class="brand__tagline">Artisan Torréfacteur</span>
    </div>
  </header>

  <h1 class="line coffee-name">N<sup>o</sup>5 de CaptainKettle</h1>
  <p class="line coffee-type">100% Arabica</p>
  <p class="line coffee-origin">(Bresil, Congo, Ethipie)</p>
  <p class="line coffee-desc">One line text goes here, lorem ipsum doler amit</p>
  <p class="line address">14, rue des Tilleuls 78000 Versailles</p>
  <p class="line phone">Tel: 01 23 45 67 89</p>
  <p class="line website">www.captainkettle.fr</p>
</main>
</body>
</html>
```